Business Card Design Project

Hello! We need a business card design for a new company opening up in Downtown Dallas called Marbrook Cupcakes. We are a cupcake factory and our primary colors are Harbor Teal and Brown. We want to have a design that can be used for multiple positions (Owner/Operations Manager, Assistant Operations Manager, Decorator, Baker, Corporate Sale Rep, Special Events Rep etc) We would like for it to be double sided. Use the following information in your designs:

Renata Vasquill
Assistant Operations Manager
renata@marbrookcupcakes.example
T555.318.9047

Store Hours:
Mon-Thur 10am-9pm
Fri-Sat 10am-10pm
Sun 12pm-7pm

website: www.marbrookcupcakes.example

Address: 2735 Quarry Ln, Dallas TX 75999

The logo is attached.

Industry/Entity Type

Business

Requirements
Must have
• It must be Harbor Teal and Brown.
Nice to have
• Nice for it to be double sided.
Should not have
• No graphics like a cupcake. Just the word logo.

```html
<!DOCTYPE html>
<html lang="en">
<head>
<meta charset="utf-8">
<title>Marbrook Cupcakes – Business Cards</title>
<link href="https://fonts.googleapis.com/css2?family=Josefin+Sans:wght@300;400&display=swap" rel="stylesheet">
<style>
  :root {
    --harbor-teal: #74f2cf;
    --teal-soft: #8ef5d9;
    --brown: #33190f;
    --brown-soft: #3e2016;
    --white: #ffffff;
    --page: #ffffff;
  }
  * { box-sizing: border-box; margin: 0; padding: 0; }
  html, body { width: 1200px; height: 850px; overflow: hidden; background: var(--page); }
  body { position: relative; font-family: "Josefin Sans", sans-serif; font-weight: 300; }

  /* Front cards */
  .front {
    position: absolute; top: 97px; width: 267px; height: 461px;
    background: var(--white);
  }
  .front-top, .front-bottom { position: absolute; left: 0; width: 100%; }
  .front-top { top: 0; height: 117px; }
  .front-top::after {
    content: ""; position: absolute; left: 0; right: 0; bottom: 3px;
    border-bottom: 1px dotted var(--white);
  }
  .front-bottom { top: 228px; height: 233px; }
  .front-bottom::before {
    content: ""; position: absolute; left: 0; right: 0; top: 3px;
    border-top: 1px dotted var(--white);
  }
  .fill-teal { background: var(--harbor-teal); }
  .fill-brown { background: var(--brown); }
  .pattern-brown { background: linear-gradient(135deg, var(--brown) 0%, var(--brown-soft) 50%, var(--brown) 100%); }
  .pattern-teal { background: linear-gradient(135deg, var(--harbor-teal) 0%, var(--teal-soft) 50%, var(--harbor-teal) 100%); }
  .accent-band {
    position: absolute; left: 0; right: 0; top: 92px; height: 13px;
    background: var(--harbor-teal);
  }
  .wordmark {
    position: absolute; top: 117px; left: 0; width: 100%; height: 111px;
    display: flex; align-items: center; justify-content: center;
    color: var(--harbor-teal); font-size: 26px; font-weight: 300; letter-spacing: 0.5px;
  }
  .address {
    position: absolute; left: 0; right: 0; bottom: 26px;
    text-align: center; font-size: 18px; line-height: 21px; font-weight: 300;
  }
  .address.on-dark { color: var(--white); }
  .address.on-light { color: var(--white); }

  /* Back cards */
  .back {
    position: absolute; top: 570px; width: 469px; height: 265px;
    color: var(--white);
  }
  .back.teal { left: 17px; background: var(--harbor-teal); }
  .back.brown { left: 495px; background: var(--brown); }
  .name-band {
    position: absolute; left: 0; right: 0; top: 11px; height: 40px;
    display: flex; align-items: center; padding-left: 26px; gap: 8px;
    font-size: 19px;
  }
  .back.teal .name-band { background: var(--brown); }
  .back.brown .name-band { background: var(--harbor-teal); }
  .back.brown .job-title { color: var(--brown); }
  .contact {
    position: absolute; top: 66px; left: 0; right: 0; text-align: center;
    font-size: 17px; line-height: 24px;
  }
  .divider {
    position: absolute; top: 128px; left: 38px; right: 38px;
    border-top: 1px dotted var(--white);
  }
  .hours-label {
    position: absolute; top: 172px; left: 64px; font-size: 18px;
  }
  .hours-list {
    position: absolute; top: 145px; left: 238px; list-style: none;
    font-size: 17px; line-height: 25px;
  }
  .website {
    position: absolute; bottom: 16px; left: 0; right: 0; text-align: center;
    font-size: 16px;
  }
</style>
</head>
<body>

  <section class="front" style="left:17px">
    <div class="front-top fill-teal"></div>
    <div class="wordmark">Marbrook Cupcakes</div>
    <div class="front-bottom fill-brown">
      <p class="address on-dark">2735 Quarry Ln<br>Dallas TX 75999</p>
    </div>
  </section>

  <section class="front" style="left:303px">
    <div class="front-top pattern-brown" role="img" aria-label="Interlocking teal ring pattern on brown"></div>
    <div class="wordmark">Marbrook Cupcakes</div>
    <div class="front-bottom pattern-teal" role="img" aria-label="Soft interlocking ring pattern on harbor teal">
      <p class="address on-light">2735 Quarry Ln<br>Dallas TX 75999</p>
    </div>
  </section>

  <section class="front" style="left:587px">
    <div class="front-top pattern-brown" role="img" aria-label="Subtle interlocking ring pattern on brown"></div>
    <div class="wordmark">Marbrook Cupcakes</div>
    <div class="front-bottom fill-teal">
      <p class="address on-light">2735 Quarry Ln<br>Dallas TX 75999</p>
    </div>
  </section>

  <section class="front" style="left:871px">
    <div class="front-top pattern-brown" role="img" aria-label="Subtle interlocking ring pattern on brown">
      <div class="accent-band"></div>
    </div>
    <div class="wordmark">Marbrook Cupcakes</div>
    <div class="front-bottom pattern-brown" role="img" aria-label="Subtle interlocking ring pattern on brown">
      <p class="address on-dark">2735 Quarry Ln<br>Dallas TX 75999</p>
    </div>
  </section>

  <section class="back teal">
    <div class="name-band"><span class="person-name">Renata Vasquill</span><span class="job-title">Assistant Operations Manager</span></div>
    <p class="contact">renata@marbrookcupcakes.example<br>555.318.9047</p>
    <div class="divider"></div>
    <p class="hours-label">Store Hours</p>
    <ul class="hours-list">
      <li>Mon-Thur 10am-9pm</li>
      <li>Fri-Sat 10am-10pm</li>
      <li>Sun 12pm-7pm</li>
    </ul>
    <p class="website">www.marbrookcupcakes.example</p>
  </section>

  <section class="back brown">
    <div class="name-band"><span class="person-name">Renata Vasquill</span><span class="job-title">Assistant Operations Manager</span></div>
    <p class="contact">renata@marbrookcupcakes.example<br>555.318.9047</p>
    <div class="divider"></div>
    <p class="hours-label">Store Hours</p>
    <ul class="hours-list">
      <li>Mon-Thur 10am-9pm</li>
      <li>Fri-Sat 10am-10pm</li>
      <li>Sun 12pm-7pm</li>
    </ul>
    <p class="website">www.marbrookcupcakes.example</p>
  </section>

</body>
</html>
```